Create an infographic for an optical business.

We need an infograph to illustrate the method and definition of how to read and understand a prescription.

Easy, straight forward, simple design of the infograph is highly desirable.
This infograph will be used for a website and on-ground marketing flyer.

Colour scheme is orange, grey, black and white.

Target Market(s)

age 18 to 35 years old

Industry/Entity Type

Business

Font styles to use
Sans Serif
Decorative

Colors
f78f20
757575
e8e8e8
000000

Requirements
Must have
• Must have a clear, simple and neat way of propagating the information on an infograph with graphics and icon to entice the interest.
Nice to have
• you may look up on the internet for stock images to further enhance the infograph. stock images of prescriptions. give me some ideas.
Should not have
• please do not populate the design with words.

```html
<!DOCTYPE html>
<html lang="en">
<head>
<meta charset="utf-8">
<title>How to Read and Enter Your Eyeglass Prescription</title>
<link href="https://fonts.googleapis.com/css2?family=Open+Sans:wght@300;400;600&display=swap" rel="stylesheet">
<style>
  :root {
    --orange: #f78f20;
    --grey: #757575;
    --grey-dark: #5e5e5e;
    --grey-light: #e8e8e8;
    --grey-soft: #d6d6d6;
    --black: #000000;
    --white: #ffffff;
  }
  * { margin: 0; padding: 0; box-sizing: border-box; }
  html, body { width: 675px; height: 1200px; overflow: hidden; background: var(--white); }
  .infographic {
    position: relative; width: 675px; height: 1200px; overflow: hidden;
    font-family: "Open Sans", Arial, sans-serif; color: var(--grey); background: var(--white);
  }
  .title-bar {
    position: absolute; left: 0; top: 0; width: 675px; height: 34px; background: var(--orange);
    color: var(--white); font-size: 14px; text-align: center; line-height: 34px; letter-spacing: .3px;
  }
  .hero {
    position: absolute; left: 0; top: 34px; width: 675px; height: 280px;
    background: linear-gradient(90deg, #b9bcc0 0%, #d3d5d8 45%, #e4e5e7 100%);
  }
  .speech-bubble { position: absolute; left: 455px; top: 70px; width: 200px; height: 120px; }
  .speech-bubble svg { position: absolute; left: 0; top: 0; }
  .speech-bubble span {
    position: absolute; left: 12px; top: 42px; width: 176px; text-align: center;
    font-size: 18px; color: var(--orange); font-weight: 400; white-space: nowrap;
  }

  .sph-header { position: absolute; left: 0; top: 318px; width: 675px; height: 64px; display: flex; align-items: center; gap: 14px; }
  .sph-header .tab {
    height: 64px; width: 150px; background: var(--grey-dark); color: var(--white);
    font-size: 32px; font-weight: 300; display: flex; align-items: center; padding-left: 26px;
    border-radius: 0 32px 32px 0;
  }
  .sph-header .sub { font-size: 22px; color: var(--grey); font-weight: 300; }
  .sph-header .rule { position: absolute; left: 150px; right: 0; top: 52px; height: 4px; background: var(--grey-dark); }

  .body-text { position: absolute; font-size: 12.5px; line-height: 20px; font-weight: 300; }
  .sph-text { left: 30px; top: 400px; width: 615px; color: var(--grey); }

  .cyl-band { position: absolute; left: 0; top: 632px; width: 675px; height: 168px; background: var(--orange); }
  .cyl-label {
    position: absolute; left: 370px; top: 648px; width: 240px; height: 40px; background: var(--white);
    color: var(--orange); font-size: 22px; font-weight: 300; line-height: 40px; padding-left: 30px;
  }
  .cyl-text { left: 30px; top: 702px; width: 615px; color: var(--white); }

  .axis-band { position: absolute; left: 0; top: 800px; width: 675px; height: 112px; background: var(--grey-light); }
  .axis-text { left: 30px; top: 820px; width: 420px; color: var(--grey); }
  .axis-figure {
    position: absolute; left: 505px; top: 808px; width: 140px; height: 80px; border-radius: 4px;
    background: linear-gradient(180deg, #f2f2f2 0%, var(--grey-soft) 100%);
  }
  .axis-label { position: absolute; left: 505px; top: 890px; width: 140px; text-align: center; font-size: 14px; color: var(--grey-dark); }

  .add-tab {
    position: absolute; left: 0; top: 922px; width: 130px; height: 30px; background: var(--grey);
    color: var(--white); font-size: 19px; font-weight: 300; line-height: 30px; padding-left: 26px;
    border-radius: 0 15px 15px 0;
  }
  .add-rule { position: absolute; left: 130px; right: 0; top: 936px; height: 3px; background: var(--grey); }
  .add-text { left: 30px; top: 958px; width: 615px; color: var(--grey); font-size: 12px; line-height: 16px; }

  .terms { position: absolute; left: 0; top: 1028px; width: 675px; height: 172px; display: flex; gap: 4px; background: var(--white); }
  .term { flex: 1; background: var(--grey-dark); color: var(--white); }
  .term h2 {
    font-size: 22px; font-weight: 300; padding: 4px 14px; background: var(--grey);
    border-bottom: 3px solid var(--orange); letter-spacing: 1px;
  }
  .term p { padding: 8px 14px; font-size: 11px; line-height: 16px; font-weight: 300; color: #e0e0e0; }
</style>
</head>
<body>
<div class="infographic">
  <header class="title-bar">How to Read and Enter Your Eyeglass Prescription</header>

  <div class="hero" role="img" aria-label="Photo of a smiling child wearing blue eyeglasses, hand on chin, against a grey backdrop"></div>
  <div class="speech-bubble">
    <svg width="200" height="120" viewBox="0 0 200 120">
      <path d="M100 8 C158 8 194 30 194 56 C194 84 158 104 100 104 C84 104 70 102 58 98 L26 114 L36 90 C16 82 6 70 6 56 C6 30 42 8 100 8 Z" fill="#ffffff" stroke="#bdbdbd" stroke-width="1.5"/>
    </svg>
    <span>Easy even for kids!</span>
  </div>

  <section>
    <div class="sph-header">
      <div class="tab">SPH</div>
      <div class="sub">(sphere)</div>
      <div class="rule"></div>
    </div>
    <p class="body-text sph-text">A plus (+) in the box indicates that you are long sighted which means you find it difficult to see things close to you. A minus (-) shows that you find it hard to see things that are far away without glasses. The number might be very small, like 0.25, or a large number, like 8.00. The higher the number, the stronger the prescription lenses required.</p>
  </section>

  <section>
    <div class="cyl-band"></div>
    <div class="cyl-label">CYL (cylinder)</div>
    <p class="body-text cyl-text">The amount of astigmatism (visual distortion) is caused by an irregularly shaped cornea. If that box is empty, it means that there is no astigmatism and your eyes are perfectly spherical, like a football. If there is a low number, like 0.25, it means that your eyes are slightly oval like a rugby ball. The more oval your eyes are, the higher the number is.</p>
  </section>

  <section>
    <div class="axis-band"></div>
    <p class="body-text axis-text">Imagine a rugby ball tilted for the edges to point at 60 degrees. That is the axis of astigmatism. The accuracy of the number is important for clearer vision.</p>
    <div class="axis-figure" role="img" aria-label="Illustration of an eye with its astigmatism axis marked"></div>
    <div class="axis-label">AXIS</div>
  </section>

  <section>
    <div class="add-tab">ADD</div>
    <div class="add-rule"></div>
    <p class="body-text add-text">If you are over 45, there may be a number where it says 'ADD'. This is your reading addition and relates to the amount of additional correction needed to focus at close distances. If a measurement is shown in this section, it means you have different prescriptions for distance and reading. Bifocal or varifocal lenses may be needed.</p>
  </section>

  <section class="terms">
    <article class="term">
      <h2>PD</h2>
      <p>PD stands for Pupillary Distance. It is the distance between the centers of both pupils of your eyes. The center is where you see, so it should line up with the optical center of your lenses for perfect vision.</p>
    </article>
    <article class="term">
      <h2>PRISM</h2>
      <p>This usually indicates that your eyes do not work well as a pair. If there is muscle imbalance between your eyes, prism lenses will provide the correction you need and help prevent headaches and double vision.</p>
    </article>
    <article class="term">
      <h2>BASE</h2>
      <p>The base simply tells the lab the direction of the prism in your lens.</p>
    </article>
  </section>
</div>
</body>
</html>
```